Motel Sign - Front

(21/03/12 - I've edited the brief and removing the words "garden view" its not fitting in the designs I'm getting and just want the word motel to be the focus. I have a template/vision of what I want - see the whiteboard sketch of what I'm looking for uploaded today. Definitely open to creatively, new designs and different ideas but the whiteboard design I've done should be a guideline. Keep it fresh/green/white. use the sample photos of green as inspiration. Thanks)
We are a motel set in the mountain country of Victoria - Australia. The front of the motel needs a fresh look. We recently removed a large amount of the garden to expose a brick courtyard fence which the front of the courtyard faces out to the main road. Within the courtyard fence there is a wooden frame and paneling.
We want to have a new sign created to slot into the wooden frame. (see photo) its the white component.
Its a very large and unusual shape and I want to keep it simple but need to fill the in the best way possible.
The space is 940mm high and 4940mm width.
The message of the sign is simple the word "MOTEL". I want people to be able to drive past and glance in and see we are a motel straight away. So the main purpose of the sign is to say "MOTEL".
I am open to colour use to match the space and have impact. I thought a background colour should be 'off white'. I'm open to the colours used to match your design as long as it matches the brief. Maybe a garden green for the emblem.
IN BRIEF:
1) the word "MOTEL"
2) Border/Background that ties in the garden.
The design should be centred, clean and simple, doesn't have to fill the whole space as long as its balanced and centred.
I like cursive and garden like designs for this one - as long its the word MOTEL still has impact. (OPEN TO NEW IDEAS)
I am also open to different ideas and suggestions if you feel you have a better way to take advantage of this space.
The sign will be 7-8 metres from the road itself.
NOTE: the photos show the space and the painted white in the space where the sign will go. The garden in front of this space will be completely cleared.

```html
<!DOCTYPE html>
<html lang="en">
<head>
<meta charset="utf-8">
<title>Motel Sign – Front</title>
<link rel="stylesheet" href="https://fonts.googleapis.com/css2?family=Playfair+Display:wght@900&display=swap">
<style>
  :root {
    --page-bg: #ffffff;
    --garden-green: #0f8a3c;
    --garden-green-light: #2fa54d;
    --garden-green-deep: #0a6b2c;
    --blossom-white: #e9f4df;
    --blossom-lime: #a9d45a;
    --letter-white: #ffffff;
    --letter-outline: #0a5a25;
  }
  html, body {
    margin: 0;
    padding: 0;
    width: 1200px;
    height: 748px;
    overflow: hidden;
    background: var(--page-bg);
  }
  .canvas {
    position: relative;
    width: 1200px;
    height: 748px;
  }
  .motel-sign {
    position: absolute;
    left: 40px;
    top: 267px;
    width: 1120px;
    height: 213px;
    overflow: hidden;
    background: linear-gradient(180deg, var(--garden-green-light) 0%, var(--garden-green) 55%, var(--garden-green-deep) 100%);
  }
  .blossom-cluster {
    position: absolute;
    top: 0;
    height: 100%;
  }
  .blossom-cluster--left {
    left: 0;
    width: 300px;
    background:
      radial-gradient(ellipse at 35% 45%, var(--blossom-white) 0%, rgba(233,244,223,0.75) 30%, rgba(169,212,90,0.45) 55%, rgba(15,138,60,0) 80%);
  }
  .blossom-cluster--right {
    right: 0;
    width: 260px;
    background:
      radial-gradient(ellipse at 62% 50%, var(--blossom-white) 0%, rgba(233,244,223,0.75) 30%, rgba(169,212,90,0.45) 55%, rgba(15,138,60,0) 80%);
  }
  .sign-word {
    position: absolute;
    inset: 0;
    width: 100%;
    height: 100%;
  }
  .sign-word text {
    font-family: 'Playfair Display', Georgia, serif;
    font-weight: 900;
    font-size: 262px;
    fill: var(--letter-white);
    stroke: var(--letter-outline);
    stroke-width: 9px;
    stroke-linejoin: round;
    paint-order: stroke fill;
  }
</style>
</head>
<body>
  <main class="canvas">
    <section class="motel-sign">
      <div class="blossom-cluster blossom-cluster--left" role="img" aria-label="Cluster of white garden blossoms and green leaves"></div>
      <div class="blossom-cluster blossom-cluster--right" role="img" aria-label="Cluster of white garden blossoms and green leaves"></div>
      <svg class="sign-word" viewBox="0 0 1120 213" aria-label="MOTEL">
        <text x="560" y="196" text-anchor="middle" textLength="790" lengthAdjust="spacingAndGlyphs">MOTEL</text>
      </svg>
    </section>
  </main>
</body>
</html>
```